Australia-Wide Industry Leader Bookkeeping Business Website Design Required

We need a website designed for our 10 year old bookkeeping business, Barwick & Lund. Barwick & Lund has been servicing the local & interstate communities of Australia, providing first-class BAS & Bookkeeping services with a personal touch unmatched by anyone else in the county.

What began 10 years ago as a small business focusing on family, friends and the local community, it has since grown into a well respected business with 95% of their business based solely on word of mouth and personal referrals from around Australia.

We would like to see designs that incorporate our existing brand/logo. The colours to be used on the website should be colours that work well with our logo. The design should communicate maturity, trust and confidence with a Web 2.0 look and feel.

We have produced mockups of the entire website as well as assets used in the mockups. Please reference the attached files. The mockups are an example of all the design elements that we want on each page. Designers are encouraged to use the mockups as a guideline only and for designers to use their own creativity.
Updates

This message is for new graphic designers who are considering commencing work on this project. Thank you for expressing an interest in our project. We would like to inform you that this project is close to completion as we have a number designs under very serious consideration.

We are currently in a position where we are disinterested providing feedback to improve on new designs submitted. We will provide feedback to improve new designs only if the submitted designs are very close to what we want for our website, and will only require 1 or 2 revision rounds to refine before the project completion date we will not work with designers to refine their newly submitted designs.

We feel that it is important for all designers to know the above information as we feel that your time and effort may be better spent working on another project.

Thank you for your understanding.

A big thank you for all the designs submitted. We are now in the process of selecting a design. Please be patient during this process. Thank you.

Target Market(s)

Busy Business Owners

Industry/Entity Type

Small Business

Requirements
Must have
• We require a rectangular "slide show" type feature to serve as a "teaser" to arouse the emotions of our website visitors. Each slide asks a specific question. The questions are:

- Is your paperwork in a mess?
- Do you need to get organised for the end of financial year?
- Are you sick & tired of endless amounts of paperwork & BASs?
- Do you feel frustrated & annoyed because you know your books need to be done?
- Do you lack the time & patience to get your paperwork done?
- Do you wish you had more time to do the things you enjoy doing?
- Contact Barwick & Lund today and we will transform your chaos into order.

Underneath the slide show will be a button to "Call Barwick & Lund Now - 03 5550 1827".

```html
<!DOCTYPE html>
<html lang="en">
<head>
<meta charset="utf-8">
<title>Barwick &amp; Lund – Why Choose Us</title>
<link rel="stylesheet" href="https://fonts.googleapis.com/css2?family=Tinos:wght@400;700&family=Arimo:wght@400;700&display=swap">
<style>
  :root {
    --bg: #eeeeee;
    --page: #ffffff;
    --text: #1f1f1f;
    --muted: #555555;
    --tick: #6aa52a;
    --accent: #c0392b;
    --rule: #cfcfcf;
    --badge-a: #2d4f8a;
    --badge-b: #b23a3a;
    --badge-c: #7a5a2e;
    --badge-d: #a83232;
    --badge-e: #8a8a8a;
    --social-a: #3b5998;
    --social-b: #33a3dd;
  }
  * { box-sizing: border-box; margin: 0; padding: 0; }
  html, body { width: 900px; height: 1200px; overflow: hidden; background: var(--bg); }
  body { font-family: "Tinos", "Times New Roman", serif; color: var(--text); }
  .page {
    position: absolute; left: 30px; top: 40px; width: 840px; height: 1120px;
    background: var(--page); border-top: 6px solid var(--rule);
    padding: 40px 36px 30px;
  }
  .columns { display: flex; gap: 30px; }
  .benefits { flex: 1 1 55%; }
  .credentials { flex: 1 1 45%; }
  .tick-list { list-style: none; }
  .tick-list > li {
    display: flex; align-items: flex-start; gap: 10px;
    font-size: 19px; line-height: 1.35; margin-bottom: 12px;
  }
  .tick-list svg { flex: 0 0 20px; width: 20px; height: 20px; margin-top: 2px; }
  .plain-item { font-size: 19px; line-height: 1.35; margin: 4px 0 12px; }
  .bullets { list-style: disc; margin: 6px 0 14px 58px; }
  .bullets li { font-size: 19px; line-height: 1.55; }
  .credentials-heading {
    font-family: "Arimo", Arial, sans-serif; font-size: 13px; font-weight: 700;
    color: var(--accent); border: 1px solid var(--accent);
    padding: 6px 10px; margin-bottom: 18px; letter-spacing: .2px;
  }
  .credentials .tick-list > li { font-size: 18px; }
  .callout {
    margin: 30px auto 0; width: 300px; border: 2px solid var(--text);
    text-align: center; padding: 12px 10px;
    font-family: "Tinos", serif; font-weight: 700; font-size: 22px;
    line-height: 1.25; color: var(--accent);
  }
  .badges {
    display: flex; justify-content: space-between; align-items: center;
    margin: 60px 10px 0; padding-bottom: 24px; border-bottom: 1px solid var(--rule);
  }
  .badge { display: block; }
  .footer { display: flex; justify-content: space-between; align-items: flex-start; margin-top: 24px; }
  .follow { display: flex; align-items: center; gap: 12px; font-family: "Arimo", Arial, sans-serif; font-size: 14px; font-weight: 700; color: var(--muted); }
  .social { display: flex; align-items: center; gap: 5px; font-family: "Tinos", serif; font-size: 15px; font-weight: 400; color: var(--text); }
  .social i { display: inline-block; width: 12px; height: 12px; }
  .social-facelink i { background: var(--social-a); }
  .social-chirper i { background: var(--social-b); }
  .legal { text-align: right; font-size: 14px; color: var(--muted); line-height: 1.6; }
</style>
</head>
<body>
<svg width="0" height="0" style="position:absolute" aria-hidden="true">
  <symbol id="tick" viewBox="0 0 20 20">
    <circle cx="10" cy="10" r="9.5" fill="var(--tick)"/>
    <path d="M5.5 10.5 L8.7 13.5 L14.5 6.8" fill="none" stroke="#fff" stroke-width="2.4" stroke-linecap="round" stroke-linejoin="round"/>
  </symbol>
</svg>

<main class="page">
  <div class="columns">
    <section class="benefits">
      <ul class="tick-list">
        <li><svg><use href="#tick"/></svg><span>The Barwick &amp; Lund Team are investors &amp; traders</span></li>
        <li><svg><use href="#tick"/></svg><span>Extensive Business Network for your benefit</span></li>
        <li><svg><use href="#tick"/></svg><span>Backed by a team of Accountants</span></li>
      </ul>
      <p class="plain-item">We work with a team of elite accountants &amp; wealth creation professionals who coach us monthly in the following:</p>
      <ul class="bullets">
        <li>Asset Protection</li>
        <li>Superannuation &amp; Self Managed Superannuation Funds</li>
        <li>Property Investing</li>
      </ul>
      <p class="plain-item">Tax Strategies, tax structures &amp; best tax savings</p>
      <p class="plain-item">We understand just how important it is to help lead &amp; guide our clients from making profits to:</p>
      <ul class="bullets">
        <li>Maximising profits</li>
        <li>Wealth creation</li>
        <li>Tax Minimization</li>
        <li>Asset Protection</li>
      </ul>
    </section>

    <section class="credentials">
      <h2 class="credentials-heading">QUALIFICATIONS, MEMBERSHIPS AND PARTNERSHIPS</h2>
      <ul class="tick-list">
        <li><svg><use href="#tick"/></svg><span>Registered Tax Office BAS Agent</span></li>
        <li><svg><use href="#tick"/></svg><span>Certificate IV Financial Services</span></li>
        <li><svg><use href="#tick"/></svg><span>Certificate III Financial Services</span></li>
        <li><svg><use href="#tick"/></svg><span>Member of Guild of Ledger Keepers</span></li>
        <li><svg><use href="#tick"/></svg><span>Platinum Member of Bookkeepers Circle</span></li>
        <li><svg><use href="#tick"/></svg><span>Ledgerly Professional Partner</span></li>
        <li><svg><use href="#tick"/></svg><span>TaxWise Collective</span></li>
      </ul>
      <p class="callout">THIS IS SOMETHING<br>OTHER BOOKKEEPERS<br>JUST DON'T DO!</p>
    </section>
  </div>

  <div class="badges">
    <svg class="badge" width="60" height="70" viewBox="0 0 60 70" aria-hidden="true"><rect x="2" y="2" width="56" height="66" rx="4" fill="var(--badge-a)"/></svg>
    <svg class="badge" width="90" height="70" viewBox="0 0 90 70" aria-hidden="true"><rect x="2" y="8" width="86" height="54" rx="6" fill="var(--badge-b)"/></svg>
    <svg class="badge" width="70" height="70" viewBox="0 0 70 70" aria-hidden="true"><circle cx="35" cy="35" r="32" fill="var(--badge-c)"/></svg>
    <svg class="badge" width="70" height="70" viewBox="0 0 70 70" aria-hidden="true"><rect x="4" y="4" width="62" height="62" rx="8" fill="var(--badge-d)"/></svg>
    <svg class="badge" width="170" height="70" viewBox="0 0 170 70" aria-hidden="true"><rect x="2" y="10" width="166" height="50" rx="3" fill="var(--badge-e)"/></svg>
  </div>

  <footer class="footer">
    <div class="follow">
      <span>FOLLOW US</span>
      <span class="social social-facelink"><i></i>Facelink</span>
      <span class="social social-chirper"><i></i>Chirper</span>
    </div>
    <div class="legal">
      <p>The content of this site are copyright © 2011, Barwick &amp; Lund. All Rights Reserved.</p>
      <p>This page was last modified Sat 29 Jan 2011.</p>
    </div>
  </footer>
</main>
</body>
</html>
```